Introduction of new dentist and new treatments

We want inform our Patients of our new dentist and new treatment methods. It is dealing about biologic dentistry and holistic dentistry. we are in switzerland and speak german

Font styles to use
Sans Serif

Colors
00a990
33b8a4
9bcb3c
acd036
cadf82
0292cd
3176b5
e34297
e667a6

Requirements
Must have
• Text, which can be edited. It will be in german
• Name of the dental clinic is
• "Velmora - Ihr Zahnarzt in Zug"
Nice to have
• A4 Layout

```html
<!DOCTYPE html>
<html lang="de">
<head>
<meta charset="utf-8">
<title>Velmora – Interdisziplinäre Zahnmedizin</title>
<link rel="stylesheet" href="https://fonts.googleapis.com/css2?family=Lato:ital,wght@0,400;0,700;0,900;1,700&family=Roboto+Condensed:wght@700&display=swap">
<style>
  :root{
    --stage:#323a3c;
    --paper:#ffffff;
    --teal:#00a990;
    --pink:#e8869f;
    --blue:#1d6fc0;
    --navy:#1c2b4a;
    --ink:#2b2b2b;
  }
  *{margin:0;padding:0;box-sizing:border-box}
  html,body{width:1200px;height:1200px;overflow:hidden;background:var(--stage)}
  .flyer{
    position:absolute;left:260px;top:82px;width:680px;height:955px;
    background:var(--paper);overflow:hidden;
    font-family:"Lato",sans-serif;color:var(--ink);
  }
  .flyer-shapes{position:absolute;inset:0;width:680px;height:955px}
  .brand{position:absolute;left:30px;top:100px;width:200px;text-align:center}
  .brand-name{font-size:23px;font-weight:400;letter-spacing:6px;color:var(--navy)}
  .brand-tagline{font-size:11.5px;font-weight:700;color:var(--navy);margin-top:6px}
  .content{position:absolute;left:40px;top:448px;width:573px}
  .headline{
    font-family:"Roboto Condensed",sans-serif;font-weight:700;
    font-size:22.5px;line-height:28px;color:var(--blue);
    width:402px;padding-bottom:8px;border-bottom:2px dotted var(--blue);
  }
  .intro{font-size:12.6px;line-height:16px;font-weight:700;font-style:italic;margin-top:13px;text-align:justify}
  .section-title{
    display:inline-block;font-size:14.6px;font-weight:700;color:var(--teal);
    padding-bottom:3px;border-bottom:1.5px dotted #777;margin-top:14px;
  }
  .section-title.wide{width:422px}
  .section-text{font-size:8.6px;line-height:11.3px;font-weight:700;text-align:justify;margin-top:7px}
</style>
</head>
<body>
  <article class="flyer">
    <svg class="flyer-shapes" viewBox="0 0 680 955">
      <defs>
        <linearGradient id="clinicTone" x1="0" y1="0" x2="1" y2="1">
          <stop offset="0" stop-color="#eef2f6"/>
          <stop offset="0.55" stop-color="#d5dde6"/>
          <stop offset="1" stop-color="#8ea0c8"/>
        </linearGradient>
        <linearGradient id="teamTone" x1="0" y1="0" x2="0" y2="1">
          <stop offset="0" stop-color="#eef1f4"/>
          <stop offset="1" stop-color="#9fb4d8"/>
        </linearGradient>
      </defs>
      <rect x="0" y="0" width="680" height="500" fill="url(#clinicTone)" role="img" aria-label="Foto: lächelnde Zahnärztin im blauen Kasack neben einer Patientin im Behandlungsstuhl, Röntgenbild auf dem Monitor"/>
      <path d="M0 0 H366 C332 112 232 192 0 206 Z" fill="var(--teal)"/>
      <path d="M0 0 H356 C322 106 220 180 0 198 Z" fill="var(--pink)"/>
      <path d="M0 0 H350 C318 100 212 170 0 182 Z" fill="var(--paper)"/>
      <path d="M0 396 C150 352 330 348 500 400 L500 460 L0 460 Z" fill="var(--teal)"/>
      <path d="M0 414 C160 374 320 370 430 402 L430 460 L0 460 Z" fill="var(--pink)"/>
      <path d="M0 428 C170 392 330 392 470 408 C560 420 630 440 680 462 V520 H0 Z" fill="var(--paper)"/>
      <path d="M0 460 H680 V960 H0 Z" fill="var(--paper)"/>
      <path d="M630 470 C650 495 668 512 680 520 V560 C660 540 640 520 612 498 Z" fill="var(--teal)"/>
      <circle cx="552" cy="428" r="114" fill="none" stroke="var(--paper)" stroke-width="1.5"/>
      <circle cx="552" cy="428" r="104" fill="url(#teamTone)" role="img" aria-label="Foto: das Praxisteam in farbigen Kasacks als Gruppe"/>
      <path d="M452 955 C540 930 620 914 680 900 V955 Z" fill="var(--blue)"/>
    </svg>

    <header class="brand">
      <div class="brand-name">VELMORA</div>
      <div class="brand-tagline">Ihr Zahnarzt in Zug</div>
    </header>

    <main class="content">
      <h1 class="headline">Interdisziplinäre Zahnmedizin -<br>Zusammenhang zwischen Zahnproblemen<br>und der Gesundheit von Körper und Geist</h1>
      <p class="intro">Zahn und Gesundheit haben eins gemeinsam – Man vermisst sie, wenn sie fehlt. Zähne haben einen engen Zusammenhang zur Gesundheit und können diese beeinflussen. Sowohl negativ als auch positiv.</p>

      <h2 class="section-title wide">Funktion des Kauorgans und interdisziplinäre Zahnmedizin</h2>
      <p class="section-text">„Funktion ist nicht alles. Aber ohne Funktion ist alles nichts!“ Sagte einst Prof. A. Gerlach (Zahnarzt, Gnathologie) und betonte die Bedeutung der Funktion des Kausystems. Sprechen, Kauen aber auch Körperhaltung und Stressmanagement gehören zu den Funktionen der Zähne. Ein gut funktionierendes Kauorgan (nach Prof. R. Steinmann, interdisziplinäre Zahnmedizin) kann Stress bewältigen und mehr Leistung und Wohlbefinden bringen. Sehr oft erkennt man Funktionsstörungen daran, dass die Zähne nicht richtig zueinander passen oder Muskelverspannungen und Schmerzen im Kiefergelenk auftreten.</p>

      <h2 class="section-title">Parodontitis und systemische Erkrankungen</h2>
      <p class="section-text">Parodontitis (Entzündung des Zahnhalteapparats) ist eine der häufigsten chronischen Krankheiten weltweit und daher gut erforscht. Herzkrankheiten, Diabetes und Frühgeburtlichkeit sind einige der systemischen Krankheiten mit der Parodontitis in Zusammenhang steht. Eine systematische Parodontitis-Behandlung kann positive Auswirkungen auf die gesamte Gesundheit haben.</p>

      <h2 class="section-title">Zahnverlust und neurologische Auswirkung</h2>
      <p class="section-text">Ein physiologisches Kausystem hat sehr feine Steuerungs- und Wahrnehmungsmöglichkeiten. Bei Zahnverlust werden diese Fähigkeiten weniger benötigt. Weniger gebrauchte Ressourcen werden von der Natur dementsprechend abgebaut. Studien zeigen, dass Menschen mit weniger Zähnen mehr Risiko zur Bildung von Demenz bergen.</p>

      <h2 class="section-title">Ganzheitliche Erklärungen</h2>
      <p class="section-text">Die komplementäre Zahnheilkunde, sehr oft auch als ganzheitliche oder biologische Zahnheilkunde bezeichnet, versucht mit Hilfe von Meridianen (Traditionelle Chinesische Medizin), den Zusammenhang zwischen Zähnen und anderen Organen und Körperteilen zu erklären. Es gibt immer mehr Patienten und Zahnärzte die von dieser Theorie und deren Ergebnissen überzeugt sind. Aufgrund der wissenschaftlichen Lage ist eine ausführliche Aufklärung vor der Behandlung sehr ratsam.</p>
    </main>
  </article>
</body>
</html>
```